Financial Advisor Resource Firm needs business card design

Need business card design for company in Omaha NE called Tallowbrook Partners. We provide resources to financial advisors....workshop programs, retirement analysis, and insurance planning. I would like to see designs that use grays, greens, black, and white colors. The final design should communicate 'collaboration' and be simple yet attractive to financial planning clients. I will attached our logo and another picture of a puzzle piece coming together. I would like the incorporate the puzzle picture somehow, maybe on the back somehow, with color or just the gray scale....OR, the picture be the front of the card with 'Tallowbrook' definition on it (see upload) and then company logo, employee name, title, address on the back (see ppt uploaded). The following disclosure needs to be included somewhere- Advisory services offered through Marlowe Ridge Advisors, LLC.
Updates

I uploaded a svg and ai file of the logo

Target Market(s)

Financial planning clients and financial advisors....so pretty diverse age range of about 40-70.

Industry/Entity Type

Financial Planning

Contact Information for Business Card

Dennis K. Holloway, MBA
Founder/President
5727 E. Larkspur Avenue
Suite 418
Omaha, NE 68297
Phone- (402) 555-0147
Cell- (402) 555-0183
Fax- (402) 555-0129
email- dennis@tallowbrookgroup.example
web address- www.tallowbrookgroup.example

Colors
1b1b1b
474747
d3d3d3
ffffff
9bcb3c
abd036

Requirements
Must have
• Must include logo provided, must be 2 sided, and must have disclosure...all of these items listed in project description

```html
<!DOCTYPE html>
<html lang="en">
<head>
<meta charset="utf-8">
<title>Tallowbrook Partners – Business Card</title>
<link rel="stylesheet" href="https://fonts.googleapis.com/css2?family=Cormorant+Garamond:wght@500&family=Open+Sans:ital,wght@0,400;1,400&family=Roboto:wght@400;500&display=swap">
<style>
  :root {
    --backdrop: #b1b2b5;
    --ink: #1b1b1b;
    --graphite: #474747;
    --mist: #d3d3d3;
    --paper: #ffffff;
    --leaf: #9bcb3c;
    --lime: #abd036;
  }
  * { box-sizing: border-box; margin: 0; padding: 0; }
  html, body { width: 1200px; height: 1200px; overflow: hidden; }
  body { background: var(--backdrop); position: relative; font-family: "Roboto", Arial, sans-serif; }

  .card { position: absolute; top: 446px; width: 540px; height: 309px; overflow: hidden; }

  /* Front */
  .card-front { left: 31px; }
  .front-photo {
    position: absolute; inset: 0;
    background:
      radial-gradient(ellipse at 70% 75%, #8a8a8a 0%, transparent 55%),
      radial-gradient(ellipse at 25% 20%, #9a9a9a 0%, transparent 50%),
      linear-gradient(135deg, #7d7d7d 0%, #6b6b6b 45%, #3e3e3e 100%);
  }
  .definition-word {
    position: absolute; top: 108px; left: 0; right: 0; text-align: center;
    font-family: "Cormorant Garamond", Georgia, serif; font-weight: 500;
    font-size: 52px; letter-spacing: 1px; color: var(--leaf); line-height: 1;
  }
  .definition-phonetic {
    position: absolute; top: 165px; left: 0; right: 0; text-align: center;
    font-family: "Open Sans", Arial, sans-serif; font-size: 15px; color: var(--paper);
  }
  .definition-meaning {
    position: absolute; top: 186px; left: 0; right: 0; text-align: center;
    font-family: "Open Sans", Arial, sans-serif; font-size: 15px; color: var(--paper);
  }

  /* Back */
  .card-back { left: 602px; background: var(--paper); }
  .holder-name {
    position: absolute; left: 316px; top: 72px;
    font-family: "Open Sans", Arial, sans-serif; font-style: italic;
    font-size: 18px; color: var(--ink);
  }
  .name-rule { position: absolute; left: 310px; right: 0; top: 99px; height: 1px; background: var(--leaf); }
  .holder-title {
    position: absolute; left: 316px; top: 101px;
    font-family: "Open Sans", Arial, sans-serif; font-size: 16px; color: var(--graphite);
  }
  .contact-list { position: absolute; left: 300px; top: 154px; list-style: none; }
  .contact-list li {
    display: flex; align-items: center; height: 18.2px;
    font-size: 14px; color: var(--ink);
  }
  .contact-list svg { width: 11px; height: 11px; margin-right: 8px; flex: none; }
  .address {
    position: absolute; left: 300px; top: 252px; display: flex; align-items: flex-start;
    font-size: 14px; color: var(--ink); line-height: 18px;
  }
  .address svg { width: 12px; height: 16px; margin: 2px 7px 0 0; flex: none; }
  .brand {
    position: absolute; left: 20px; top: 246px; display: flex; align-items: center; gap: 8px;
    font-family: "Roboto", Arial, sans-serif; font-weight: 500; font-size: 19px; color: var(--ink);
  }
  .brand-dot { width: 14px; height: 14px; border-radius: 50%; background: var(--leaf); }
  .disclosure {
    position: absolute; left: 20px; top: 276px;
    font-family: "Roboto", Arial, sans-serif; font-size: 9px; color: var(--graphite);
  }
  .base-band { position: absolute; left: 0; bottom: 0; width: 540px; height: 12px; }
</style>
</head>
<body>

<section class="card card-front">
  <div class="front-photo" role="img" aria-label="Grayscale photograph of several hands joining puzzle pieces together"></div>
  <div class="definition-word">TALLOW·BROOK</div>
  <div class="definition-phonetic">ˈtal·ō·bro͝ok</div>
  <div class="definition-meaning">: to come together and unite in common interest and focus</div>
</section>

<section class="card card-back">
  <div class="holder-name">Dennis K. Holloway, MBA</div>
  <div class="name-rule"></div>
  <div class="holder-title">Founder/President</div>

  <ul class="contact-list">
    <li>
      <svg viewBox="0 0 12 12"><path d="M1 5c0-2 2-3 5-3s5 1 5 3H8V4H4v1z M3 6h6l1 4H2z" fill="var(--leaf)"/></svg>
      (402) 555-0147
    </li>
    <li>
      <svg viewBox="0 0 12 12"><path d="M2 1l2 0 1 3-1.5 1c.7 1.5 1.8 2.6 3.3 3.3L8 7l3 1v2c-5 0-9-4-9-9z" fill="none" stroke="var(--leaf)" stroke-width="1"/></svg>
      (402) 555-0183
    </li>
    <li>
      <svg viewBox="0 0 12 12"><rect x="3" y="1" width="6" height="4" fill="none" stroke="var(--leaf)"/><rect x="1" y="5" width="10" height="6" fill="none" stroke="var(--leaf)"/><rect x="4" y="7" width="4" height="2" fill="var(--leaf)"/></svg>
      (402) 555-0129
    </li>
    <li>
      <svg viewBox="0 0 12 12"><rect x="0.5" y="2.5" width="11" height="7" fill="none" stroke="var(--leaf)"/><path d="M.5 2.5l5.5 4 5.5-4" fill="none" stroke="var(--leaf)"/></svg>
      dennis@tallowbrookgroup.example
    </li>
    <li>
      <svg viewBox="0 0 12 12"><circle cx="6" cy="6" r="5" fill="none" stroke="var(--leaf)"/><ellipse cx="6" cy="6" rx="2.2" ry="5" fill="none" stroke="var(--leaf)"/><path d="M1 6h10" stroke="var(--leaf)"/></svg>
      www.tallowbrookgroup.example
    </li>
  </ul>

  <div class="address">
    <svg viewBox="0 0 12 16"><path d="M6 15C3 11 1 8.5 1 6a5 5 0 0 1 10 0c0 2.5-2 5-5 9z" fill="none" stroke="var(--leaf)" stroke-width="1.2"/><circle cx="6" cy="6" r="2" fill="none" stroke="var(--leaf)" stroke-width="1.2"/></svg>
    <span>5727 E. Larkspur Avenue<br>Suite 418, Omaha, NE 68297</span>
  </div>

  <div class="brand">
    <span class="brand-dot"></span>
    <span>Tallowbrook Partners</span>
  </div>
  <p class="disclosure">Advisory services offered through Marlowe Ridge Advisors, LLC.</p>

  <svg class="base-band" viewBox="0 0 540 12" preserveAspectRatio="none">
    <polygon points="0,0 316,0 308,12 0,12" fill="var(--ink)"/>
    <polygon points="316,0 540,0 540,12 308,12" fill="var(--leaf)"/>
  </svg>
</section>

</body>
</html>
```